New startup requiring business card

New company needed a business card / logo. Company name is
Minthel
Company is providing IT software sales, partnering and consulting services across the APAC region. Catch line is "growing together".
We currently have a feeling yellow as the primary colour given its meaning across the region but open to ideas. Main brief is we want something smart, clean and professional while still leveraging the strength of the name.
A major part of the business is mutually beneficial partnerships, not sure if this helps but maybe visual around linkages between objects.
Also wanting a standard size card, preference is something that will have a D/S cello sheen finish in a matt. But again open to ideas, wow us!
Software

```html
<!DOCTYPE html>
<html lang="en">
<head>
<meta charset="utf-8">
<title>Minthel – Business Card</title>
<link href="https://fonts.googleapis.com/css2?family=Varela+Round&display=swap" rel="stylesheet">
<style>
  :root {
    --navy: #14303f;
    --navy-deep: #0f2633;
    --sky: #a9d4ea;
    --sky-soft: #b9dcee;
    --sky-pale: #c4dfee;
    --lime: #d5d43a;
    --paper: #f7f7f4;
    --ink: #1c2f3c;
    --mist: #dfe7ec;
    --chip: #eef3f6;
    --muted: #cfdde6;
    --stage: #e8e5e0;
  }
  * { box-sizing: border-box; margin: 0; padding: 0; }
  html, body { width: 1200px; height: 697px; overflow: hidden; }
  body { background: var(--stage); position: relative; font-family: "Varela Round", sans-serif; }

  .wordmark { font-family: "Varela Round", sans-serif; font-weight: 400; letter-spacing: 1px; line-height: 1; }
  .catchline { font-family: "Varela Round", sans-serif; font-weight: 400; letter-spacing: .5px; line-height: 1; }

  /* Brand panel */
  .brand-panel {
    position: absolute; left: 20px; top: 30px; width: 490px; height: 175px;
    background: #fff; border-radius: 16px;
    display: flex; align-items: center; gap: 26px; padding-left: 48px;
  }
  .brand-dot { width: 58px; height: 58px; border-radius: 50%; background: var(--lime); flex: none; }
  .brand-panel .wordmark { font-size: 60px; color: var(--ink); }
  .brand-panel .catchline { font-size: 20px; color: #3a3a3a; margin-top: 12px; }

  /* Contact card */
  .contact-card {
    position: absolute; left: 610px; top: 40px; width: 560px; height: 320px;
    background: var(--paper); overflow: hidden; box-shadow: 0 2px 6px rgba(0,0,0,.15);
  }
  .contact-card .brand { position: absolute; left: 150px; top: 34px; display: flex; align-items: center; gap: 18px; }
  .contact-card .brand-dot { width: 42px; height: 42px; }
  .contact-card .wordmark { font-size: 44px; color: var(--ink); }
  .contact-card .catchline { font-size: 16px; color: #3a3a3a; margin-top: 8px; }
  .contact-card .backdrop { position: absolute; left: 0; top: 140px; }
  .person { position: absolute; left: 46px; top: 180px; color: var(--ink); transform: rotate(-2deg); }
  .person-name { font-size: 20px; letter-spacing: 1px; }
  .person-title { font-size: 13px; font-style: italic; margin-top: 4px; margin-left: 12px; }
  .contacts { position: absolute; left: 300px; top: 160px; list-style: none; }
  .contacts li { display: flex; align-items: center; gap: 8px; margin-bottom: 10px; }
  .contacts svg { flex: none; }
  .contacts span {
    background: var(--chip); border-radius: 10px; padding: 5px 14px;
    font-size: 14px; color: var(--ink); min-width: 210px; line-height: 1.25;
  }

  /* Front card */
  .front-card {
    position: absolute; left: 150px; top: 375px; width: 560px; height: 310px;
    background: var(--navy); overflow: hidden; box-shadow: 0 2px 6px rgba(0,0,0,.2);
  }
  .front-card .brand { position: absolute; left: 40px; top: 28px; display: flex; align-items: center; gap: 24px; }
  .front-card .brand-dot { width: 64px; height: 64px; }
  .front-card .wordmark { font-size: 54px; color: var(--mist); }
  .front-card .catchline { font-size: 20px; color: var(--sky); margin-top: 10px; }
  .phone-band {
    position: absolute; left: 0; top: 132px; width: 100%; height: 72px;
    background: var(--sky-soft); display: flex; align-items: center; justify-content: center;
    font-size: 50px; color: var(--navy-deep); letter-spacing: 1px;
  }
  .services { position: absolute; top: 224px; width: 100%; text-align: center; color: var(--muted); font-size: 14px; letter-spacing: 1.5px; }
  .reach { position: absolute; top: 250px; width: 100%; text-align: center; color: var(--muted); font-size: 14px; font-style: italic; letter-spacing: .5px; }
</style>
</head>
<body>

  <section class="brand-panel">
    <div class="brand-dot"></div>
    <div>
      <div class="wordmark">Minthel</div>
      <div class="catchline">growing together</div>
    </div>
  </section>

  <section class="contact-card">
    <div class="brand">
      <div class="brand-dot"></div>
      <div>
        <div class="wordmark">Minthel</div>
        <div class="catchline">growing together</div>
      </div>
    </div>
    <svg class="backdrop" width="560" height="180" viewBox="0 0 560 180">
      <rect width="560" height="180" fill="var(--sky)"/>
      <polygon points="0,12 270,0 210,180 0,180" fill="var(--lime)"/>
      <polygon points="0,12 90,8 0,70" fill="var(--sky-pale)"/>
    </svg>
    <div class="person">
      <div class="person-name">ALEX MARLOW</div>
      <div class="person-title">Title here</div>
    </div>
    <ul class="contacts">
      <li>
        <svg width="22" height="22" viewBox="0 0 22 22"><circle cx="11" cy="11" r="10" fill="#fff"/><path d="M8 6 7 16M14 6 13 16M5.5 9h11M5 13h11" stroke="var(--ink)" stroke-width="1.6"/></svg>
        <span>555-014-2760</span>
      </li>
      <li>
        <svg width="22" height="22" viewBox="0 0 22 22"><circle cx="11" cy="11" r="10" fill="#fff"/><circle cx="11" cy="11" r="3" fill="none" stroke="var(--ink)" stroke-width="1.6"/><path d="M14 8v4.5c0 1.5 2.5 1.5 2.5-1.5a5.5 5.5 0 1 0-2 4.3" fill="none" stroke="var(--ink)" stroke-width="1.6"/></svg>
        <span>alex@minthel.com</span>
      </li>
      <li>
        <svg width="22" height="22" viewBox="0 0 22 22"><circle cx="11" cy="11" r="10" fill="#fff"/><path d="M11 17s-4.5-4.5-4.5-7.5a4.5 4.5 0 0 1 9 0C15.5 12.5 11 17 11 17z" fill="var(--ink)"/><circle cx="11" cy="9.5" r="1.6" fill="#fff"/></svg>
        <span>72 Orchard Ave.<br>City, ST 000000</span>
      </li>
    </ul>
  </section>

  <section class="front-card">
    <div class="brand">
      <div class="brand-dot"></div>
      <div>
        <div class="wordmark">Minthel</div>
        <div class="catchline">growing together</div>
      </div>
    </div>
    <div class="phone-band">555-014-2760</div>
    <p class="services">SOFTWARE SALES &nbsp;•&nbsp; PARTNERING &nbsp;•&nbsp; CONSULTING SERVICES</p>
    <p class="reach">- Offering superior services across the APAC region -</p>
  </section>

</body>
</html>
```